complete redesign of VitaPlate.com

VITAPLATE.COM
MAIN MANU

We need it cut into HTML / Wordpress Friendly.... Our developer will handle all the WP / PHP coding, but we need it placed into HTML format so he can put into wordpress.

Please see the old vitaplate.com by visiting www.vitaplate.com... we want something completely different, but... just use this site for reference as to audience, theme, etc... we want something where it is science meets diet in helping fight cancer :)

WE NEED SOMETHING MORE MODERN AND MEDICAL IN TERMS OF DESIGN

See below:

1 CANCER NEWS
2 NUTRITION DIAGNOSTICS
3 DIET STEPS
4 DIET SUPPLEMENTS IN CANCER 
5 DICTIONARY OF MARKINGS ON FOOD
6 MERIVOLA VIDEOS
7 YOUR INDIVIDUAL DIET - SUBSCRIPTION

a. CANCER NEWS - latest articles relating to cancer prevention research treatments

b. NUTRITION DIAGNOSTICS -  description of the research that must be done to determine the degree of malnutrition of the body a place on the charts
pictures, etc.

c. DIET STEPS 
(sub menu - @)
¥ prevention of oncological - @
¥ diet chemotherapy - @
¥ diet in radiotherapy - @
¥ hormonal diet - @
¥ diet during convalescence - @

d. DIET SUPPLEMENTS IN CANCER - articles describing various supplements summary tables, etc.

e. DICTIONARY OF MARKINGS ON FOOD - composition, translation of labels on food, itd.

f. MERIVOLA VIDEOS 
(sub menu - @)
¥ healthy cooking - @
¥ meal preparation - @
¥ storage of food - @
¥ eco food - @
¥ rehabilitation - @
¥ yoga - @
¥ exercises - @
¥ psycho-oncology training - @
¥ music therapy - @

g. YOUR INDIVIDUAL DIET -  individual personalized diet for subscribing. We
add this point by developing a system of diet.

After 3 months, we will add special individual programs that mix diet, exercise and psychological lectures

Industry/Entity Type

Medical

Logo Text

Vita Plate / VitaPlate.com

Number of Pages Required

5+ page

Font styles to use
Sans Serif

Colors
ec1f27
9bcb3c
ffffff

Requirements
Must have
• HTML/CSS

```html
<!DOCTYPE html>
<html lang="en">
<head>
<meta charset="utf-8">
<title>VitaPlate</title>
<link href="https://fonts.googleapis.com/css2?family=Signika:wght@300;400;600&display=swap" rel="stylesheet">
<style>
:root{
  --green:#6dca6d;
  --green-dark:#55a552;
  --green-btn:#5fb35c;
  --black:#111;
  --grey-bg:#ebebeb;
  --text:#222;
  --muted:#666;
  --white:#fff;
}
*{box-sizing:border-box;margin:0;padding:0}
html,body{width:705px;height:1200px;overflow:hidden;background:var(--white)}
body{font-family:"Signika",Arial,sans-serif;color:var(--text);position:relative}
.wrap{position:absolute;left:101px;width:502px}

/* header */
.site-header{top:0;height:53px}
.brand{position:absolute;left:0;top:17px;display:flex;align-items:center;gap:6px}
.brand-dot{width:14px;height:14px;border-radius:50%;background:var(--green)}
.brand-name{font-size:17px;font-weight:600;color:var(--text)}
.connect{position:absolute;left:290px;top:30px;font-size:6px;color:#333;letter-spacing:.2px}
.phone{position:absolute;right:0;top:26px;font-size:10px;display:flex;align-items:center;gap:4px}
.main-nav{top:53px;height:29px;background:var(--green);display:flex}
.main-nav a{flex:auto;color:var(--white);font-size:6px;text-align:center;text-decoration:none;display:flex;align-items:center;justify-content:center;line-height:1.3;border-right:1px solid rgba(255,255,255,.35);padding:0 4px}
.main-nav a:last-child{border-right:none}

/* hero */
.hero{position:absolute;left:0;top:82px;width:705px;height:228px;background:radial-gradient(ellipse at 50% 20%,#8a8077,#4c4540 60%,#2f2a28)}
.hero-title{position:absolute;left:246px;top:103px;width:210px;height:41px;background:rgba(20,20,20,.78);color:var(--white);font-size:25px;font-weight:300;text-align:center;line-height:41px;letter-spacing:1px}
.hero-dots{position:absolute;left:317px;top:283px;display:flex;gap:4px}
.hero-dots span{width:6px;height:6px;border-radius:50%;background:var(--white)}
.hero-dots span:first-child{background:#3aa0d8}

/* heading blocks */
.block-head{position:absolute;top:346px;height:46px;padding:8px 10px;font-size:12.5px;font-weight:600;line-height:1.3;letter-spacing:.3px}
.news-head{left:101px;width:288px;background:var(--green);color:var(--white)}
.video-head{left:402px;width:201px;background:var(--black);color:var(--green);padding-left:12px}
.video-arrows{position:absolute;right:12px;top:16px}

/* news */
.news-item{position:absolute;left:101px;width:288px;height:82px}
.news-thumb{position:absolute;left:0;top:0;width:114px;height:82px}
.news-body{position:absolute;left:122px;top:0;width:166px}
.news-meta{font-size:4.5px;color:var(--muted);margin-bottom:6px}
.news-meta b{color:var(--text);font-weight:600}
.news-title{font-size:5.6px;font-weight:600;line-height:1.9;padding-left:7px}
.news-excerpt{font-size:5.6px;line-height:1.9;padding-left:7px}
.news-item.tight .news-title,.news-item.tight .news-excerpt{padding-left:0}
.read-more{display:inline-block;margin-top:4px;background:var(--green-btn);color:var(--white);font-size:5.5px;padding:3px 4px}
.view-all{position:absolute;left:101px;top:727px;width:288px;height:28px;background:var(--black);color:var(--green);font-size:7.5px;text-align:center;line-height:28px;font-weight:600}

/* videos */
.video-card{position:absolute;left:402px;width:201px;height:105px}
.video-caption{position:absolute;left:0;bottom:0;width:100%;height:23px;background:rgba(20,20,20,.75);color:var(--green);font-size:7px;font-weight:600;padding-left:9px;line-height:23px}
.play{position:absolute;left:92px;top:40px}

/* diet steps */
.steps{position:absolute;left:0;top:786px;width:705px;height:200px;background:var(--grey-bg)}
.steps h2{position:absolute;top:26px;width:100%;text-align:center;font-size:12.5px;font-weight:600}
.steps-tabs{position:absolute;left:102px;top:54px;width:115px;background:var(--white)}
.steps-tabs li{list-style:none;font-size:5.6px;color:#555;height:22.4px;line-height:22.4px;padding-left:11px}
.steps-tabs li.active{background:var(--green);color:var(--white)}
.steps-image{position:absolute;left:230px;top:54px;width:165px;height:111px}
.steps-text{position:absolute;left:401px;top:55px;width:202px;font-size:5.6px;line-height:1.9}
.steps-text p+p{margin-top:8px}

/* subscribe */
.subscribe{position:absolute;left:0;top:986px;width:705px;height:150px;background:var(--green-dark);color:var(--white);text-align:center}
.subscribe h2{margin-top:27px;font-size:17px;font-weight:600}
.subscribe p{margin:8px auto 0;width:422px;font-size:5.6px;line-height:1.9}
.subscribe-form{position:absolute;left:186px;top:99px;display:flex;gap:13px}
.subscribe-input{width:245px;height:20px;background:var(--white);color:#888;font-size:5.3px;text-align:left;padding-left:6px;line-height:20px}
.subscribe-btn{width:74px;height:20px;background:#222;font-size:5.6px;font-weight:600;line-height:20px}

/* footer */
.site-footer{position:absolute;left:0;top:1136px;width:705px;height:64px;text-align:center}
.footer-nav{margin-top:20px;font-size:5.6px;color:var(--text)}
.footer-nav span{margin:0 4px}
.copyright{margin-top:12px;font-size:5.3px}
</style>
</head>
<body>

<header class="wrap site-header">
  <div class="brand"><span class="brand-dot"></span><span class="brand-name">VitaPlate</span></div>
  <div class="connect">CONNECT WITH US</div>
  <div class="phone">
    <svg width="7" height="7" viewBox="0 0 24 24"><path fill="#6dca6d" d="M6.6 10.8a15 15 0 0 0 6.6 6.6l2.2-2.2c.3-.3.7-.4 1-.2 1.1.4 2.3.6 3.6.6.6 0 1 .4 1 1V20c0 .6-.4 1-1 1A17 17 0 0 1 3 4c0-.6.4-1 1-1h3.5c.6 0 1 .4 1 1 0 1.3.2 2.5.6 3.6.1.3 0 .7-.2 1z"/></svg>
    1-800-555-0142
  </div>
</header>

<nav class="wrap main-nav">
  <a href="#">CANCER<br>NEWS</a>
  <a href="#">NUTRITION<br>DIAGNOSTICS</a>
  <a href="#">DIET<br>STEPS</a>
  <a href="#">DIET SUPPLEMENTS<br>IN CANCER</a>
  <a href="#">DICTIONARY OF<br>MARKINGS ON FOOD</a>
  <a href="#">MERIVOLA<br>VIDEOS</a>
  <a href="#">YOUR INDIVIDUAL<br>DIET -SUBSCRIPTION</a>
</nav>

<section class="hero" role="img" aria-label="Microscopic view of cells with virus particles">
  <div class="hero-title">VITA PLATE</div>
  <div class="hero-dots"><span></span><span></span><span></span><span></span></div>
</section>

<div class="block-head news-head">VITA PLATE<br>NEWS</div>
<div class="block-head video-head">MERIVOLA<br>VIDEOS
  <svg class="video-arrows" width="20" height="10" viewBox="0 0 20 10"><path d="M5 1 1 5l4 4M15 1l4 4-4 4" stroke="#fff" stroke-width="1.6" fill="none"/></svg>
</div>

<article class="news-item" style="top:410px">
  <div class="news-thumb" role="img" aria-label="Potatoes with carved letters" style="background:linear-gradient(135deg,#c9a66e,#8a6a3e)"></div>
  <div class="news-body">
    <div class="news-meta">DECEMBER 15TH, 2015 &nbsp;|&nbsp; <b>POSTED BY VITA PLATE</b></div>
    <div class="news-title">LOREM IPSUM IS SIMPLY DUMMY TEXT OF THE PRINTING AND TYPESETTING INDUSTRY.</div>
    <div class="news-excerpt">Lorem Ipsum has been the industry's standard dummy text ever since the 1500s, when an unknown printer took a galley of type and scrambled it to make a type specimen book.</div>
    <span class="read-more">READ MORE</span>
  </div>
</article>

<article class="news-item tight" style="top:521px">
  <div class="news-thumb" role="img" aria-label="Plate of vegetable rice dish" style="background:linear-gradient(135deg,#6b3a2a,#c96a3a 55%,#8fae5a)"></div>
  <div class="news-body">
    <div class="news-meta">DECEMBER 15TH, 2015 &nbsp;|&nbsp; <b>POSTED BY VITA PLATE</b></div>
    <div class="news-title">LOREM IPSUM IS SIMPLY DUMMY TEXT OF THE PRINTING AND TYPESETTING INDUSTRY.</div>
    <div class="news-excerpt">Lorem Ipsum has been the industry's standard dummy text ever since the 1500s, when an unknown printer took a galley of type and scrambled it to make a type specimen book.</div>
    <span class="read-more">READ MORE</span>
  </div>
</article>

<article class="news-item tight" style="top:632px">
  <div class="news-thumb" role="img" aria-label="Strawberries, blueberries and supplement capsules" style="background:linear-gradient(135deg,#c2202a,#7a1a30 60%,#3a3a7a)"></div>
  <div class="news-body">
    <div class="news-meta">DECEMBER 15TH, 2015 &nbsp;|&nbsp; <b>POSTED BY VITA PLATE</b></div>
    <div class="news-title">LOREM IPSUM IS SIMPLY DUMMY TEXT OF THE PRINTING AND TYPESETTING INDUSTRY.</div>
    <div class="news-excerpt">Lorem Ipsum has been the industry's standard dummy text ever since the 1500s, when an unknown printer took a galley of type and scrambled it to make a type specimen book.</div>
    <span class="read-more">READ MORE</span>
  </div>
</article>

<div class="view-all">VIEW LATEST ARTICLES</div>

<div class="video-card" style="top:410px;background:linear-gradient(135deg,#8a6a4a,#d9b98a 50%,#5a8a3a)" role="img" aria-label="Bowls of fresh salad">
  <svg class="play" width="18" height="18" viewBox="0 0 18 18"><circle cx="9" cy="9" r="7.5" fill="none" stroke="#fff" stroke-width="1.5"/><path d="M7 5.5v7l5.5-3.5z" fill="#fff"/></svg>
  <div class="video-caption">HEALTHY COOKING - @</div>
</div>
<div class="video-card" style="top:530px;background:linear-gradient(135deg,#e8e8e8,#9aa3ad 55%,#5a6470)" role="img" aria-label="Couple preparing a meal in a kitchen">
  <svg class="play" width="18" height="18" viewBox="0 0 18 18"><circle cx="9" cy="9" r="7.5" fill="none" stroke="#fff" stroke-width="1.5"/><path d="M7 5.5v7l5.5-3.5z" fill="#fff"/></svg>
  <div class="video-caption">MEAL PREPARATION - @</div>
</div>
<div class="video-card" style="top:649px;background:linear-gradient(90deg,#5a2a0a,#c86a1a 45%,#e08a2a 70%,#7a3a10)" role="img" aria-label="Jars of preserved food">
  <svg class="play" width="18" height="18" viewBox="0 0 18 18"><circle cx="9" cy="9" r="7.5" fill="none" stroke="#fff" stroke-width="1.5"/><path d="M7 5.5v7l5.5-3.5z" fill="#fff"/></svg>
  <div class="video-caption">STORAGE OF FOOD</div>
</div>

<section class="steps">
  <h2>DIET STEPS</h2>
  <ul class="steps-tabs">
    <li class="active">PREVENTION OF ONCOLOGICAL - @</li>
    <li>DIET CHEMOTHERAPY - @</li>
    <li>DIET IN RADIOTHERAPY - @</li>
    <li>HORMONAL DIET - @</li>
    <li>DIET DURING CONVALESCENCE - @</li>
  </ul>
  <div class="steps-image" role="img" aria-label="Microscopic illustration of a cancer cell with immune cells" style="background:radial-gradient(circle at 45% 45%,#d0602a,#7a1a1a 50%,#3a0a0a)"></div>
  <div class="steps-text">
    <p>Lorem Ipsum is simply dummy text of the printing and typesetting industry. Lorem Ipsum has been the industry's standard dummy text ever since the 1500s, when an unknown printer took a galley of type and scrambled it to make a type specimen book. It has survived not only five centuries, but also the leap into electronic typesetting, remaining essentially unchanged.</p>
    <p>It was popularised in the 1960s with the release of Typeline sheets containing Lorem Ipsum passages, and more recently with desktop publishing software like Pagecraft Studio including versions of Lorem Ipsum.</p>
  </div>
</section>

<section class="subscribe">
  <h2>YOUR INDIVIDUAL DIET</h2>
  <p>individual personalized diet for subscribing. We add this point by developing a system of diet.After 3 months, we will add special individual programs that mix diet, exercise and psychological lectures</p>
  <div class="subscribe-form">
    <div class="subscribe-input">Enter Your E-Mail Address</div>
    <div class="subscribe-btn">SUBSCRIBE NOW</div>
  </div>
</section>

<footer class="site-footer">
  <div class="footer-nav">CANCER NEWS<span>|</span>DIET STEPS<span>|</span>4 DIET SUPPLEMENTS IN CANCER<span>|</span>DICTIONARY OF MARKINGS ON FOOD<span>|</span>MERIVOLA VIDEOS<span>|</span>YOUR INDIVIDUAL DIET - SUBSCRIPTION</div>
  <div class="copyright">© COMPANY NAME &nbsp;| ALL RIGHTS RESERVED</div>
</footer>

</body>
</html>
```